Business Card for Orvane Parts Wholesale supplier

Hi There! I need a new business card for our company. We are specialized in selling Orvane parts, mostly we sell new LCD screens for Telvox and Slatrons. I would like to see that back in the design.

You can find the colors and logo's on our website: www.dorvak-example.nl

Industry/Entity Type

Business

Contact Information for Business Card

My Details:
Lars Vintorp

Phone: 0031612873406
E-mail: Lars@dorvak-example.nl

Slogan: "Parts Built For Repairs"

Font styles to use
Sans Serif

Colors

Designer to choose colors to be used in the design.

Requirements
Must have
• A Black backside with the Dorvak logo on it. The front side should be clean with only my contact details.
• But I'm also open for something really different or awesome!
Nice to have
• Remember that we are in the parts & repairing industry, So i'll be handing those business cards mainly to repair companies. Maybe you can do something with that thought :)

```html
<!DOCTYPE html>
<html lang="en">
<head>
<meta charset="utf-8">
<title>Dorvak Business Card</title>
<link href="https://fonts.googleapis.com/css2?family=Open+Sans:wght@400;600;700&display=swap" rel="stylesheet">
<style>
  :root {
    --canvas: #e9e7e4;
    --card-white: #ffffff;
    --brand-orange: #e8671f;
    --brand-orange-deep: #cf5518;
    --ink: #111111;
    --text-grey: #555555;
    --mark-grey: #a9a9a9;
    --rule: #f0c7a8;
  }
  * { box-sizing: border-box; margin: 0; padding: 0; }
  html, body {
    width: 1200px; height: 1200px; overflow: hidden;
    background: var(--canvas);
    font-family: "Open Sans", Arial, sans-serif;
  }
  .sheet {
    width: 1200px; height: 1200px;
    display: flex; flex-direction: column;
    align-items: center; justify-content: center; gap: 56px;
  }
  .card {
    width: 900px; height: 514px;
    position: relative;
    box-shadow: 0 6px 18px rgba(0,0,0,0.12);
    overflow: hidden;
  }
  /* Front */
  .card-front { background: var(--card-white); }
  .contact-block { position: absolute; left: 70px; top: 110px; }
  .person-name {
    color: var(--brand-orange);
    font-weight: 700; font-size: 34px; letter-spacing: 2px;
    text-transform: uppercase; margin-bottom: 26px;
  }
  .contact-list { list-style: none; }
  .contact-item {
    display: flex; align-items: center; gap: 16px;
    color: var(--text-grey); font-size: 24px; line-height: 1; margin-bottom: 18px;
  }
  .contact-icon {
    width: 24px; height: 24px; border-radius: 4px;
    background: var(--brand-orange);
    display: flex; align-items: center; justify-content: center; flex: none;
  }
  .contact-icon svg { width: 16px; height: 16px; }
  .divider {
    position: absolute; left: 70px; top: 356px;
    width: 380px; height: 1px; background: var(--rule);
  }
  .brand-lockup {
    position: absolute; right: 70px; bottom: 70px;
    display: flex; flex-direction: column; align-items: flex-end;
  }
  .tagline { font-size: 17px; color: var(--ink); margin-bottom: 2px; margin-right: 4px; }
  .brand-row { display: flex; align-items: center; gap: 14px; }
  .brand-square { width: 58px; height: 58px; background: var(--brand-orange); }
  .brand-name { font-weight: 700; font-size: 82px; line-height: 1; color: var(--ink); letter-spacing: 1px; }
  /* Back */
  .card-back {
    background: linear-gradient(120deg, var(--brand-orange) 0%, var(--brand-orange-deep) 100%);
    display: flex; align-items: center; justify-content: center;
  }
  .card-back .brand-square { background: var(--mark-grey); width: 78px; height: 78px; }
  .card-back .brand-name { font-size: 108px; }
  .card-back .brand-row { gap: 20px; }
</style>
</head>
<body>
<main class="sheet">
  <section class="card card-front" aria-label="Business card front">
    <div class="contact-block">
      <h1 class="person-name">Lars Vintorp</h1>
      <ul class="contact-list">
        <li class="contact-item">
          <span class="contact-icon"><svg viewBox="0 0 16 16"><path d="M4 2h3l1 3-2 1a8 8 0 0 0 4 4l1-2 3 1v3c0 1-1 2-2 2A11 11 0 0 1 2 4c0-1 1-2 2-2z" fill="#fff"/></svg></span>
          0031612873406
        </li>
        <li class="contact-item">
          <span class="contact-icon"><svg viewBox="0 0 16 16"><rect x="2" y="4" width="12" height="8" fill="none" stroke="#fff" stroke-width="1.5"/><path d="M2 4l6 5 6-5" fill="none" stroke="#fff" stroke-width="1.5"/></svg></span>
          Lars@dorvak-example.nl
        </li>
        <li class="contact-item">
          <span class="contact-icon"><svg viewBox="0 0 16 16"><circle cx="8" cy="8" r="5.5" fill="none" stroke="#fff" stroke-width="1.4"/><path d="M2.5 8h11M8 2.5c-3 3-3 8 0 11M8 2.5c3 3 3 8 0 11" fill="none" stroke="#fff" stroke-width="1.2"/></svg></span>
          www.dorvak-example.nl
        </li>
      </ul>
    </div>
    <div class="divider"></div>
    <div class="brand-lockup">
      <p class="tagline">Parts Built For Repairs</p>
      <div class="brand-row">
        <span class="brand-square"></span>
        <span class="brand-name">dorvak</span>
      </div>
    </div>
  </section>

  <section class="card card-back" aria-label="Business card back">
    <div class="brand-row">
      <span class="brand-square"></span>
      <span class="brand-name">dorvak</span>
    </div>
  </section>
</main>
</body>
</html>
```